2021 Beatwalker's Statute Compendium

Each year I public a law book for Massachusetts Police Officers, along with an accompanying motor vehicle cruiser guide. They have the same/similar design but the motor vehicle guide has a motor vehicle twist to it. The main book with be full-size with a front, back and spine. The accompanying cruiser guide will be smaller 5X7 with a spiral binding.
The year should be somewhat prominent so people know it is a new year edition. I attached some previous versions and commonly used logos.

Target Market(s)

Police Departments, Police Officers

Requirements
Must have
• Accompanying motor vehicle cruiser guide design, can be the same with a slight modification to gear it toward motor vehicle laws/rules.

The year of publishing - 2021
Nice to have
• Real images
Should not have
• Foreign (non-US) images of police.

```html
<!DOCTYPE html>
<html lang="en">
<head>
<meta charset="UTF-8">
<title>Cruiser Guide – Back Cover</title>
<link href="https://fonts.googleapis.com/css2?family=Exo+2:wght@300;400&display=swap" rel="stylesheet">
<style>
  :root {
    --paper: #ffffff;
    --ink-dark: #0b0c0f;
    --steel: #2b2e34;
    --thin-blue: #2a3778;
    --panel: rgba(38, 36, 40, 0.86);
    --copy: #ebebeb;
    --mark: #000000;
  }
  html, body {
    margin: 0;
    padding: 0;
    width: 970px;
    height: 1200px;
    overflow: hidden;
    background: var(--paper);
  }
  .sheet {
    position: relative;
    width: 970px;
    height: 1200px;
    background: var(--paper);
  }
  .print-marks {
    position: absolute;
    inset: 0;
    width: 970px;
    height: 1200px;
  }
  .cover-art {
    position: absolute;
    left: 45px;
    top: 45px;
    width: 862px;
    height: 1110px;
    background:
      linear-gradient(150deg, transparent 55%, rgba(42, 55, 120, 0.55) 64%, transparent 72%),
      linear-gradient(150deg, #15181c 0%, #3a3e44 30%, #111317 48%, #2c3035 70%, #0c0d10 100%),
      var(--ink-dark);
  }
  .blurb-panel {
    position: absolute;
    left: 187px;
    top: 371px;
    width: 366px;
    height: 729px;
    background: var(--panel);
    box-sizing: border-box;
    padding: 36px 20px 0 42px;
  }
  .blurb-panel p {
    margin: 0 0 22.4px;
    font-family: "Exo 2", sans-serif;
    font-weight: 300;
    font-size: 16.6px;
    line-height: 22.4px;
    letter-spacing: 0.35px;
    color: var(--copy);
    white-space: nowrap;
  }
</style>
</head>
<body>
<div class="sheet">
  <div class="cover-art" role="img" aria-label="Distressed black and grey American flag with a thin blue line stripe, waving diagonally"></div>

  <div class="blurb-panel">
    <p>This motor vehicle guide is the<br>ultimate cruiser companion! It has<br>everything a Massachusetts Police<br>Officer needs to know when enforcing<br>motor vehicle laws and rules.</p>
    <p>From minor violations like defective<br>equipment; areas of more complexity<br>such as international operators,<br>to serious offenses like motor<br>vehicle homicide; you’ll find the<br>entire gamut covered here in an<br>easy to understand format.</p>
    <p>This invaluable resource has been by<br>a well-reputed working police officer<br>and attorney, making it the only<br>manual of its kind offering the kind<br>of insight that a reputable career<br>in both these frontline positions<br>defending law and order can offer.</p>
    <p>A comprehensive reference of<br>critical topics such as arrest powers,<br>fine amounts, as well as the laws<br>involving vehicle impoundments,<br>exit orders and even motor vehicle<br>searches, this is the only motor<br>vehicle cruiser guide you will need!</p>
  </div>

  <svg class="print-marks" viewBox="0 0 970 1200" aria-hidden="true">
    <g stroke="var(--mark)" stroke-width="0.7" fill="none">
      <!-- crop lines -->
      <line x1="63" y1="18" x2="63" y2="50"/><line x1="18" y1="63" x2="38" y2="63"/>
      <line x1="907" y1="18" x2="907" y2="50"/><line x1="932" y1="63" x2="952" y2="63"/>
      <line x1="63" y1="1150" x2="63" y2="1182"/><line x1="18" y1="1137" x2="38" y2="1137"/>
      <line x1="907" y1="1150" x2="907" y2="1182"/><line x1="932" y1="1137" x2="952" y2="1137"/>
      <line x1="18" y1="45" x2="38" y2="45"/><line x1="45" y1="18" x2="45" y2="38"/>
      <line x1="932" y1="45" x2="952" y2="45"/><line x1="925" y1="18" x2="925" y2="38"/>
      <line x1="18" y1="1155" x2="38" y2="1155"/><line x1="45" y1="1162" x2="45" y2="1182"/>
      <line x1="932" y1="1155" x2="952" y2="1155"/><line x1="925" y1="1162" x2="925" y2="1182"/>
    </g>
    <g stroke="var(--mark)" stroke-width="0.9" fill="none">
      <g transform="translate(485 34)"><circle r="10"/><circle r="6" fill="var(--mark)"/><line x1="-13" y1="0" x2="13" y2="0" stroke="#fff"/><line x1="0" y1="-13" x2="0" y2="13" stroke="#fff"/><line x1="-13" y1="0" x2="-6" y2="0"/><line x1="6" y1="0" x2="13" y2="0"/><line x1="0" y1="-13" x2="0" y2="-6"/><line x1="0" y1="6" x2="0" y2="13"/></g>
      <g transform="translate(485 1166)"><circle r="10"/><circle r="6" fill="var(--mark)"/><line x1="-13" y1="0" x2="13" y2="0" stroke="#fff"/><line x1="0" y1="-13" x2="0" y2="13" stroke="#fff"/><line x1="-13" y1="0" x2="-6" y2="0"/><line x1="6" y1="0" x2="13" y2="0"/><line x1="0" y1="-13" x2="0" y2="-6"/><line x1="0" y1="6" x2="0" y2="13"/></g>
      <g transform="translate(34 601)"><circle r="10"/><circle r="6" fill="var(--mark)"/><line x1="-13" y1="0" x2="13" y2="0" stroke="#fff"/><line x1="0" y1="-13" x2="0" y2="13" stroke="#fff"/><line x1="-13" y1="0" x2="-6" y2="0"/><line x1="6" y1="0" x2="13" y2="0"/><line x1="0" y1="-13" x2="0" y2="-6"/><line x1="0" y1="6" x2="0" y2="13"/></g>
      <g transform="translate(936 601)"><circle r="10"/><circle r="6" fill="var(--mark)"/><line x1="-13" y1="0" x2="13" y2="0" stroke="#fff"/><line x1="0" y1="-13" x2="0" y2="13" stroke="#fff"/><line x1="-13" y1="0" x2="-6" y2="0"/><line x1="6" y1="0" x2="13" y2="0"/><line x1="0" y1="-13" x2="0" y2="-6"/><line x1="0" y1="6" x2="0" y2="13"/></g>
    </g>
  </svg>
</div>
</body>
</html>
```